Brenton Wealth Management Flow Charts

I need help creating three flow charts for my businesses website. We want them to be simple but look professional. This is for a Wealth Management firm. I will attach a word document that has all of the descriptions for everything so you know what icons to use. We just want the chart to have an icon, the names of each step and the corresponding numbers. I will also include some examples of charts we liked as well. Once the winner is selected, we will need help with additional graphic design elements for our website ASAP.
- Goudy Roman

```html
<!DOCTYPE html>
<html lang="en">
<head>
<meta charset="utf-8">
<title>Planning Process Charts</title>
<link href="https://fonts.googleapis.com/css2?family=Josefin+Sans:wght@300;400&family=Questrial&display=swap" rel="stylesheet">
<style>
  :root {
    --bg: #161616;
    --rule: #5a5a5a;
    --text: #ffffff;
    --muted: #d9d9d9;
    --c1: #f8a93a;
    --c2: #f5814f;
    --c3: #f05a5b;
    --c4: #e93b6c;
    --c5: #c32c8b;
    --c6: #8e2fa0;
  }
  html, body { margin: 0; padding: 0; overflow: hidden; background: var(--bg); }
  .canvas { width: 1200px; height: 4057px; position: relative; background: var(--bg); }
  svg { display: block; }
  .section-title { font-family: "Questrial", sans-serif; fill: var(--text); font-size: 56px; filter: url(#glow); }
  .step-num { font-family: "Josefin Sans", sans-serif; font-weight: 300; fill: var(--text); font-size: 62px; }
  .step-label { font-family: "Questrial", sans-serif; fill: var(--text); font-size: 31px; }
  .invest-label { font-family: "Questrial", sans-serif; fill: var(--text); font-size: 32px; letter-spacing: 0.5px; }
  .legacy-label { font-family: "Questrial", sans-serif; fill: var(--muted); font-size: 26px; }
  .axis-num { font-family: "Josefin Sans", sans-serif; fill: var(--muted); font-size: 30px; }
  .dots { stroke: var(--text); stroke-width: 4; stroke-dasharray: 0 11; stroke-linecap: round; }
</style>
</head>
<body>
<div class="canvas">
<svg width="1200" height="4057" viewBox="0 0 1200 4057" xmlns="http://www.w3.org/2000/svg">
  <defs>
    <filter id="glow" x="-10%" y="-50%" width="120%" height="200%">
      <feGaussianBlur stdDeviation="3" result="b"/>
      <feMerge><feMergeNode in="b"/><feMergeNode in="SourceGraphic"/></feMerge>
    </filter>
  </defs>

  <!-- Retirement planning process -->
  <g class="retirement-process">
    <text class="section-title" x="617" y="133" text-anchor="middle">The Retirement Planning Process</text>
    <circle cx="584" cy="183" r="10" fill="var(--text)"/>
    <line class="dots" x1="584" y1="200" x2="584" y2="1565"/>
    <polyline points="560,1560 584,1584 608,1560" fill="none" stroke="var(--text)" stroke-width="4"/>

    <g class="step">
      <circle cx="584" cy="331" r="74" fill="var(--bg)" stroke="var(--c1)" stroke-width="4"/>
      <circle cx="584" cy="331" r="30" fill="var(--text)" role="img" aria-label="Icon: people meeting"/>
      <line x1="426" y1="305" x2="450" y2="305" stroke="var(--c1)" stroke-width="2"/>
      <text class="step-num" x="392" y="360">01</text>
      <line x1="690" y1="295" x2="690" y2="375" stroke="var(--c1)" stroke-width="2"/>
      <text class="step-label" x="702" y="325">Discovery</text>
      <text class="step-label" x="702" y="365">meeting</text>
    </g>
    <g class="step">
      <circle cx="584" cy="551" r="74" fill="var(--bg)" stroke="var(--c2)" stroke-width="4"/>
      <circle cx="584" cy="551" r="30" fill="var(--text)" role="img" aria-label="Icon: group learning"/>
      <line x1="480" y1="520" x2="480" y2="578" stroke="var(--c2)" stroke-width="2"/>
      <text class="step-label" x="465" y="558" text-anchor="end">Learning</text>
      <line x1="732" y1="518" x2="756" y2="518" stroke="var(--c2)" stroke-width="2"/>
      <text class="step-num" x="696" y="574">02</text>
    </g>
    <g class="step">
      <circle cx="584" cy="769" r="74" fill="var(--bg)" stroke="var(--c3)" stroke-width="4"/>
      <circle cx="584" cy="769" r="30" fill="var(--text)" role="img" aria-label="Icon: people at a planning board"/>
      <line x1="428" y1="740" x2="452" y2="740" stroke="var(--c3)" stroke-width="2"/>
      <text class="step-num" x="392" y="796">03</text>
      <line x1="690" y1="742" x2="690" y2="796" stroke="var(--c3)" stroke-width="2"/>
      <text class="step-label" x="702" y="780">Planning</text>
    </g>
    <g class="step">
      <circle cx="584" cy="984" r="74" fill="var(--bg)" stroke="var(--c4)" stroke-width="4"/>
      <circle cx="584" cy="984" r="30" fill="var(--text)" role="img" aria-label="Icon: hands joining puzzle pieces"/>
      <line x1="480" y1="955" x2="480" y2="1010" stroke="var(--c4)" stroke-width="2"/>
      <text class="step-label" x="460" y="993" text-anchor="end">Exection</text>
      <line x1="732" y1="953" x2="756" y2="953" stroke="var(--c4)" stroke-width="2"/>
      <text class="step-num" x="696" y="1008">04</text>
    </g>
    <g class="step">
      <circle cx="584" cy="1202" r="74" fill="var(--bg)" stroke="var(--c5)" stroke-width="4"/>
      <circle cx="584" cy="1202" r="30" fill="var(--text)" role="img" aria-label="Icon: two people at a table"/>
      <line x1="428" y1="1175" x2="452" y2="1175" stroke="var(--c5)" stroke-width="2"/>
      <text class="step-num" x="392" y="1230">05</text>
      <line x1="690" y1="1175" x2="690" y2="1229" stroke="var(--c5)" stroke-width="2"/>
      <text class="step-label" x="702" y="1214">Alignment</text>
    </g>
    <g class="step">
      <circle cx="584" cy="1418" r="74" fill="var(--bg)" stroke="var(--c6)" stroke-width="4"/>
      <circle cx="584" cy="1418" r="30" fill="var(--text)" role="img" aria-label="Icon: person reviewing with a laptop"/>
      <line x1="480" y1="1390" x2="480" y2="1446" stroke="var(--c6)" stroke-width="2"/>
      <text class="step-label" x="460" y="1428" text-anchor="end">Review</text>
      <line x1="732" y1="1390" x2="756" y2="1390" stroke="var(--c6)" stroke-width="2"/>
      <text class="step-num" x="696" y="1446">06</text>
    </g>
  </g>

  <line x1="0" y1="1696" x2="1200" y2="1696" stroke="var(--rule)" stroke-width="2"/>

  <!-- Investment management -->
  <g class="investment-management">
    <text class="section-title" x="619" y="1839" text-anchor="middle">Comprehensive Investment Management</text>

    <g class="row" transform="translate(0,1997)">
      <line x1="314" y1="-34" x2="338" y2="-34" stroke="var(--c1)" stroke-width="2"/>
      <text class="step-num" x="280" y="22">01</text>
      <rect x="375" y="-52" width="10" height="104" fill="var(--c1)"/>
      <line x1="390" y1="-90" x2="390" y2="90" stroke="var(--rule)" stroke-width="2"/>
      <line x1="422" y1="-90" x2="422" y2="90" stroke="var(--rule)" stroke-width="2"/>
      <polygon points="424,-52 480,-52 512,0 480,52 424,52" fill="var(--c1)"/>
      <line x1="512" y1="0" x2="545" y2="-52" stroke="var(--c1)" stroke-width="3"/>
      <line x1="545" y1="-52" x2="825" y2="-52" stroke="var(--c1)" stroke-width="3"/>
      <line x1="825" y1="-52" x2="922" y2="-52" stroke="var(--c1)" stroke-width="1"/>
      <line x1="899" y1="-50" x2="899" y2="50" stroke="var(--c1)" stroke-width="2"/>
      <polyline points="891,42 899,52 907,42" fill="none" stroke="var(--c1)" stroke-width="2"/>
      <rect x="440" y="-22" width="38" height="44" rx="3" fill="none" stroke="var(--text)" stroke-width="2" role="img" aria-label="Icon: candlestick chart"/>
      <text class="invest-label" x="551" y="-8">Understanding your</text>
      <text class="invest-label" x="551" y="32">Risk Tolerance</text>
    </g>

    <g class="row" transform="translate(0,2241)">
      <line x1="314" y1="-34" x2="338" y2="-34" stroke="var(--c2)" stroke-width="2"/>
      <text class="step-num" x="280" y="22">02</text>
      <rect x="375" y="-52" width="10" height="104" fill="var(--c2)"/>
      <line x1="390" y1="-90" x2="390" y2="90" stroke="var(--rule)" stroke-width="2"/>
      <line x1="422" y1="-90" x2="422" y2="90" stroke="var(--rule)" stroke-width="2"/>
      <polygon points="424,-52 480,-52 512,0 480,52 424,52" fill="var(--c2)"/>
      <line x1="512" y1="0" x2="545" y2="-52" stroke="var(--c2)" stroke-width="3"/>
      <line x1="545" y1="-52" x2="825" y2="-52" stroke="var(--c2)" stroke-width="3"/>
      <line x1="825" y1="-52" x2="922" y2="-52" stroke="var(--c2)" stroke-width="1"/>
      <line x1="897" y1="-50" x2="897" y2="50" stroke="var(--c2)" stroke-width="2"/>
      <polyline points="889,42 897,52 905,42" fill="none" stroke="var(--c2)" stroke-width="2"/>
      <ellipse cx="459" cy="2" rx="24" ry="18" fill="none" stroke="var(--text)" stroke-width="2" role="img" aria-label="Icon: piggy bank"/>
      <text class="invest-label" x="535" y="12">Investment Selection</text>
    </g>

    <g class="row" transform="translate(0,2485)">
      <line x1="314" y1="-34" x2="338" y2="-34" stroke="var(--c3)" stroke-width="2"/>
      <text class="step-num" x="280" y="22">03</text>
      <rect x="375" y="-52" width="10" height="104" fill="var(--c3)"/>
      <line x1="390" y1="-90" x2="390" y2="90" stroke="var(--rule)" stroke-width="2"/>
      <line x1="422" y1="-90" x2="422" y2="90" stroke="var(--rule)" stroke-width="2"/>
      <polygon points="424,-52 480,-52 512,0 480,52 424,52" fill="var(--c3)"/>
      <line x1="512" y1="0" x2="545" y2="-52" stroke="var(--c3)" stroke-width="3"/>
      <line x1="545" y1="-52" x2="825" y2="-52" stroke="var(--c3)" stroke-width="3"/>
      <line x1="825" y1="-52" x2="922" y2="-52" stroke="var(--c3)" stroke-width="1"/>
      <line x1="897" y1="-50" x2="897" y2="50" stroke="var(--c3)" stroke-width="2"/>
      <polyline points="889,42 897,52 905,42" fill="none" stroke="var(--c3)" stroke-width="2"/>
      <g class="icon-pie" fill="none" stroke="var(--text)" stroke-width="2">
        <circle cx="456" cy="2" r="21"/>
        <path d="M460,-2 L460,-22 A21,21 0 0 1 480,-2 Z"/>
        <line x1="456" y1="2" x2="438" y2="12"/>
      </g>
      <text class="invest-label" x="569" y="12">Asset Allocation</text>
    </g>

    <g class="row" transform="translate(0,2729)">
      <line x1="314" y1="-34" x2="338" y2="-34" stroke="var(--c4)" stroke-width="2"/>
      <text class="step-num" x="280" y="22">04</text>
      <rect x="375" y="-52" width="10" height="104" fill="var(--c4)"/>
      <line x1="390" y1="-90" x2="390" y2="90" stroke="var(--rule)" stroke-width="2"/>
      <line x1="422" y1="-90" x2="422" y2="90" stroke="var(--rule)" stroke-width="2"/>
      <polygon points="424,-52 480,-52 512,0 480,52 424,52" fill="var(--c4)"/>
      <line x1="512" y1="0" x2="545" y2="-52" stroke="var(--c4)" stroke-width="3"/>
      <line x1="545" y1="-52" x2="825" y2="-52" stroke="var(--c4)" stroke-width="3"/>
      <line x1="825" y1="-52" x2="922" y2="-52" stroke="var(--c4)" stroke-width="1"/>
      <line x1="899" y1="-50" x2="899" y2="50" stroke="var(--c4)" stroke-width="2"/>
      <polyline points="891,42 899,52 907,42" fill="none" stroke="var(--c4)" stroke-width="2"/>
      <g class="icon-percent" fill="none" stroke="var(--text)" stroke-width="2">
        <circle cx="446" cy="-8" r="6"/>
        <circle cx="468" cy="12" r="6"/>
        <line x1="440" y1="18" x2="474" y2="-14"/>
      </g>
      <text class="invest-label" x="576" y="12">Tax efficiency</text>
    </g>

    <g class="row" transform="translate(0,2974)">
      <line x1="314" y1="-34" x2="338" y2="-34" stroke="var(--c5)" stroke-width="2"/>
      <text class="step-num" x="280" y="22">05</text>
      <rect x="375" y="-52" width="10" height="104" fill="var(--c5)"/>
      <line x1="390" y1="-90" x2="390" y2="90" stroke="var(--rule)" stroke-width="2"/>
      <line x1="422" y1="-90" x2="422" y2="90" stroke="var(--rule)" stroke-width="2"/>
      <polygon points="424,-52 480,-52 512,0 480,52 424,52" fill="var(--c5)"/>
      <line x1="512" y1="0" x2="545" y2="-52" stroke="var(--c5)" stroke-width="3"/>
      <line x1="545" y1="-52" x2="825" y2="-52" stroke="var(--c5)" stroke-width="3"/>
      <line x1="825" y1="-52" x2="922" y2="-52" stroke="var(--c5)" stroke-width="1"/>
      <line x1="899" y1="-50" x2="899" y2="50" stroke="var(--c5)" stroke-width="2"/>
      <polyline points="891,42 899,52 907,42" fill="none" stroke="var(--c5)" stroke-width="2"/>
      <rect x="438" y="-16" width="34" height="32" rx="3" fill="none" stroke="var(--text)" stroke-width="2" role="img" aria-label="Icon: coins and dollar"/>
      <text class="invest-label" x="576" y="-7">Distribution</text>
      <text class="invest-label" x="576" y="34">Strategy</text>
    </g>

    <g class="row" transform="translate(0,3218)">
      <line x1="314" y1="-34" x2="338" y2="-34" stroke="var(--c6)" stroke-width="2"/>
      <text class="step-num" x="280" y="22">06</text>
      <rect x="375" y="-52" width="10" height="104" fill="var(--c6)"/>
      <line x1="390" y1="-90" x2="390" y2="90" stroke="var(--rule)" stroke-width="2"/>
      <line x1="422" y1="-90" x2="422" y2="90" stroke="var(--rule)" stroke-width="2"/>
      <polygon points="424,-52 480,-52 512,0 480,52 424,52" fill="var(--c6)"/>
      <line x1="512" y1="0" x2="545" y2="-52" stroke="var(--c6)" stroke-width="3"/>
      <line x1="545" y1="-52" x2="825" y2="-52" stroke="var(--c6)" stroke-width="3"/>
      <line x1="825" y1="-52" x2="922" y2="-52" stroke="var(--c6)" stroke-width="1"/>
      <line x1="899" y1="-50" x2="899" y2="50" stroke="var(--c6)" stroke-width="2"/>
      <polyline points="891,42 899,52 907,42" fill="none" stroke="var(--c6)" stroke-width="2"/>
      <rect x="440" y="-24" width="30" height="48" rx="8" fill="none" stroke="var(--text)" stroke-width="2" role="img" aria-label="Icon: coach"/>
      <text class="invest-label" x="551" y="-6">Behavior Finance</text>
      <text class="invest-label" x="551" y="32">Coaching</text>
    </g>
  </g>

  <!-- Legacy and estate planning -->
  <g class="legacy-planning">
    <text class="section-title" x="622" y="3508" text-anchor="middle" style="font-size:46px">Legacy and Estate Planning</text>
    <line x1="94" y1="3780" x2="1108" y2="3780" stroke="var(--rule)" stroke-width="2"/>
    <polyline points="1094,3766 1108,3780 1094,3794" fill="none" stroke="var(--muted)" stroke-width="2"/>
    <g stroke="var(--rule)" stroke-width="2">
      <line x1="130" y1="3772" x2="130" y2="3788"/>
      <line x1="323" y1="3772" x2="323" y2="3788"/>
      <line x1="500" y1="3772" x2="500" y2="3788"/>
      <line x1="703" y1="3772" x2="703" y2="3788"/>
      <line x1="904" y1="3772" x2="904" y2="3788"/>
    </g>

    <g class="item">
      <rect x="196" y="3668" width="52" height="50" fill="none" stroke="var(--text)" stroke-width="2" role="img" aria-label="Icon: pen nib signing"/>
      <rect x="181" y="3740" width="84" height="9" fill="var(--c1)"/>
      <rect x="181" y="3754" width="84" height="3" fill="var(--c1)"/>
      <text class="axis-num" x="222" y="3792" text-anchor="middle">01</text>
      <line x1="151" y1="3825" x2="172" y2="3825" stroke="var(--c1)" stroke-width="2"/>
      <text class="legacy-label" x="151" y="3857">Beneficiaries</text>
    </g>
    <g class="item">
      <g fill="none" stroke="var(--text)" stroke-width="2" class="icon-key">
        <circle cx="428" cy="3680" r="14"/>
        <line x1="418" y1="3690" x2="392" y2="3716"/>
        <line x1="400" y1="3708" x2="408" y2="3716"/>
      </g>
      <rect x="374" y="3740" width="84" height="9" fill="var(--c2)"/>
      <rect x="374" y="3754" width="84" height="3" fill="var(--c2)"/>
      <text class="axis-num" x="414" y="3792" text-anchor="middle">02</text>
      <line x1="376" y1="3825" x2="397" y2="3825" stroke="var(--c2)" stroke-width="2"/>
      <text class="legacy-label" x="376" y="3857">Trust</text>
    </g>
    <g class="item">
      <g fill="none" stroke="var(--text)" stroke-width="2" class="icon-house">
        <polyline points="570,3690 603,3660 636,3690"/>
        <rect x="578" y="3684" width="50" height="36"/>
        <text x="603" y="3712" text-anchor="middle" fill="var(--text)" stroke="none" font-family="Questrial, sans-serif" font-size="22">%</text>
      </g>
      <rect x="562" y="3740" width="84" height="9" fill="var(--c3)"/>
      <rect x="562" y="3754" width="84" height="3" fill="var(--c3)"/>
      <text class="axis-num" x="597" y="3792" text-anchor="middle">03</text>
      <line x1="539" y1="3825" x2="560" y2="3825" stroke="var(--c3)" stroke-width="2"/>
      <text class="legacy-label" x="539" y="3857">Estate Taxes</text>
      <text class="legacy-label" x="539" y="3888">&amp; Assessment</text>
    </g>
    <g class="item">
      <rect x="780" y="3668" width="56" height="52" fill="none" stroke="var(--text)" stroke-width="2" role="img" aria-label="Icon: hand holding a heart"/>
      <rect x="766" y="3740" width="84" height="9" fill="var(--c4)"/>
      <rect x="766" y="3754" width="84" height="3" fill="var(--c4)"/>
      <text class="axis-num" x="810" y="3792" text-anchor="middle">04</text>
      <line x1="756" y1="3825" x2="777" y2="3825" stroke="var(--c4)" stroke-width="2"/>
      <text class="legacy-label" x="756" y="3857">Annual</text>
      <text class="legacy-label" x="756" y="3888">giving</text>
    </g>
    <g class="item">
      <rect x="970" y="3670" width="56" height="48" fill="none" stroke="var(--text)" stroke-width="2" role="img" aria-label="Icon: hands around a heart"/>
      <rect x="960" y="3740" width="84" height="9" fill="var(--c6)"/>
      <rect x="960" y="3754" width="84" height="3" fill="var(--c6)"/>
      <text class="axis-num" x="1002" y="3792" text-anchor="middle">05</text>
      <line x1="930" y1="3825" x2="951" y2="3825" stroke="var(--c5)" stroke-width="2"/>
      <text class="legacy-label" x="930" y="3857">Donation &amp;</text>
      <text class="legacy-label" x="930" y="3888">Charity</text>
    </g>
  </g>
</svg>
</div>
</body>
</html>
```